Email Notification & Marketing Templates

I want to start with something like a newsletter or informational email, but i need Top Tips to Detect Phishing Scams. Something that i can send to users so they can follow it when receiving or exchanging emails. I will also need promotional items for my company that i can send to customers as well. It can be based on on our website PLVORIX.COM

Will also need:
newsletters
announcements
marketing emails
alerts
security notifications

Examples:Items such as Security Awareness Poster Series
Phishing Awareness
Password Security
Email Attachments
QR Code scams
Public WiFi safety

```html
<!DOCTYPE html>
<html lang="en">
<head>
<meta charset="utf-8">
<title>Top Tips to Detect Phishing Scams – Plvorix</title>
<link rel="stylesheet" href="https://fonts.googleapis.com/css2?family=Montserrat:wght@600;700;800&family=Arimo:wght@400;700&display=swap">
<style>
  :root {
    --page-bg: #f1f2f3;
    --sheet-bg: #ffffff;
    --brand-green: #3fa535;
    --brand-green-dark: #2b8a25;
    --ink: #111111;
    --body-ink: #2a2a2a;
    --alert-red: #c8372d;
    --panel-bg: #eceef0;
    --panel-edge: #e1e4e7;
    --muted: #8a8d90;
    --rule: #dcdcdc;
  }
  * { box-sizing: border-box; margin: 0; padding: 0; }
  html, body { width: 1200px; height: 1200px; overflow: hidden; }
  body {
    background: var(--page-bg);
    font-family: "Arimo", Arial, sans-serif;
    color: var(--body-ink);
    position: relative;
  }
  .email-sheet {
    position: absolute;
    left: 285px; top: 0;
    width: 630px; height: 1200px;
    background: var(--sheet-bg);
    box-shadow: 0 0 18px rgba(0,0,0,0.08);
  }
  .brand {
    position: absolute;
    top: 48px; left: 0; width: 100%;
    display: flex; justify-content: center; align-items: center; gap: 12px;
  }
  .brand-dot {
    width: 22px; height: 22px;
    border-radius: 50%;
    background: var(--brand-green);
  }
  .brand-name {
    font-family: "Montserrat", sans-serif;
    font-weight: 700;
    font-size: 38px;
    color: var(--ink);
  }
  .hero-art {
    position: absolute;
    top: 135px; left: 0; width: 630px; height: 225px;
    background: radial-gradient(ellipse at 50% 45%, #d7f0d0 0%, #eef7ec 38%, #fbf3f2 70%, #ffffff 100%);
  }
  .headline {
    position: absolute;
    top: 382px; left: 0; width: 100%;
    text-align: center;
    font-family: "Montserrat", sans-serif;
    font-weight: 800;
    font-size: 53px;
    line-height: 62px;
    color: var(--ink);
  }
  .tips-panel {
    position: absolute;
    top: 533px; left: 17px;
    width: 596px; height: 492px;
    background: var(--panel-bg);
    border: 1px solid var(--panel-edge);
    border-radius: 12px;
    padding: 16px 12px 16px 22px;
    list-style: none;
    display: flex; flex-direction: column; justify-content: space-between;
  }
  .tip {
    display: flex; align-items: flex-start; gap: 18px;
  }
  .tip-icon {
    flex: none;
    width: 48px; height: 48px;
    border-radius: 8px;
    margin-top: 1px;
  }
  .tip-icon.is-neutral { background: linear-gradient(135deg, #cfd6de, #8e9aa6); }
  .tip-icon.is-alert { background: linear-gradient(135deg, #f3b3a8, #d9553f); }
  .tip-icon.is-link { background: linear-gradient(135deg, #d9dde2, #9aa4ae); }
  .tip-icon.is-url { background: linear-gradient(135deg, #cfe0f1, #5b87b5); }
  .tip-icon.is-card { background: linear-gradient(135deg, #bcd2ef, #e06a48); }
  .tip-icon.is-typo { background: linear-gradient(135deg, #d3e7f2, #f2b84a); }
  .tip-icon.is-safe { background: linear-gradient(135deg, #c9e8c2, #3fa535); }
  .tip-text {
    font-size: 17px;
    line-height: 22px;
    letter-spacing: -0.15px;
    color: var(--body-ink);
  }
  .tip-title { font-weight: 700; color: var(--ink); }
  .tip-title.is-alert, .tip-text .is-alert { color: var(--alert-red); }
  .cta-button {
    position: absolute;
    top: 1047px; left: 17px;
    width: 596px; height: 52px;
    border-radius: 26px;
    background: linear-gradient(180deg, #5cbf45 0%, var(--brand-green) 55%, var(--brand-green-dark) 100%);
    display: flex; align-items: center; justify-content: center;
    font-family: "Montserrat", sans-serif;
    font-weight: 700;
    font-size: 22px;
    color: #ffffff;
    text-decoration: none;
  }
  .footer-rule {
    position: absolute;
    top: 1131px; left: 17px; width: 596px;
    border-top: 1px solid var(--rule);
  }
  .social-links {
    position: absolute;
    top: 1155px; left: 17px;
    display: flex; gap: 10px;
  }
  .social-dot {
    width: 24px; height: 24px; border-radius: 50%;
    background: var(--muted);
    opacity: 0.7;
  }
  .footer-contact {
    position: absolute;
    top: 1148px; right: 17px;
    text-align: right;
    font-size: 14.5px; line-height: 19px;
    color: var(--ink);
  }
</style>
</head>
<body>
  <main class="email-sheet">
    <header>
      <div class="brand">
        <span class="brand-dot" aria-hidden="true"></span>
        <span class="brand-name">Plvorix</span>
      </div>
    </header>

    <div class="hero-art" role="img" aria-label="Illustration of a glowing green security shield with a padlock and envelope, surrounded by faded warning triangles and suspicious email snippets with underlined links"></div>

    <h1 class="headline">Top Tips to Detect<br>Phishing Scams</h1>

    <ul class="tips-panel">
      <li class="tip">
        <span class="tip-icon is-neutral" role="img" aria-label="Hooded hacker at a laptop icon"></span>
        <p class="tip-text"><span class="tip-title">Suspicious Sender Address:</span> Check for misspellings, unusual domains, or emails from unknown sources.</p>
      </li>
      <li class="tip">
        <span class="tip-icon is-alert" role="img" aria-label="Warning sign with clock icon"></span>
        <p class="tip-text"><span class="tip-title is-alert">Urgent or Threatening Language:</span> Be wary of emails demanding immediate action or threatening consequences.</p>
      </li>
      <li class="tip">
        <span class="tip-icon is-link" role="img" aria-label="Broken chain link icon"></span>
        <p class="tip-text"><span class="tip-title">Fake Links &amp; Attachments:</span> Do not click on unexpected links or download attachments from unverified senders.</p>
      </li>
      <li class="tip">
        <span class="tip-icon is-url" role="img" aria-label="Browser address bar with magnifier icon"></span>
        <p class="tip-text"><span class="tip-title is-alert">Mismatched URLs:</span> Hover over links to see the actual destination address before clicking. It should match the context.</p>
      </li>
      <li class="tip">
        <span class="tip-icon is-card" role="img" aria-label="Payment card with question bubble icon"></span>
        <p class="tip-text"><span class="tip-title">Unusual Requests for Information:</span> Legitimate companies rarely ask for sensitive data via email.</p>
      </li>
      <li class="tip">
        <span class="tip-icon is-typo" role="img" aria-label="Misspelled text speech bubble icon"></span>
        <p class="tip-text"><span class="tip-title">Poor Grammar &amp; Spelling:</span> Many phishing emails contain noticeable errors.</p>
      </li>
      <li class="tip">
        <span class="tip-icon is-safe" role="img" aria-label="Hand holding a phone with a shield icon"></span>
        <p class="tip-text"><span class="tip-title">When in Doubt, <span class="is-alert">Don't Click:</span></span> If something feels off, verify through official channels.</p>
      </li>
    </ul>

    <a class="cta-button" href="#">Stay Protected</a>

    <footer>
      <div class="footer-rule"></div>
      <div class="social-links" aria-label="Social links">
        <span class="social-dot"></span>
        <span class="social-dot"></span>
        <span class="social-dot"></span>
        <span class="social-dot"></span>
      </div>
      <p class="footer-contact">Plvorix Group<br>Email: info@plvorix.com</p>
    </footer>
  </main>
</body>
</html>
```